Design Large Inspirational Artwork with Long Quote

Design a large piece of art with a quote from Marcus Hallwell.

QUOTE
"The thing that's so interesting about being alive is that you're all in. No matter what you do, you're all in. This is gonna kill you, so I think you might as well play the most magnificent game you can while you're waiting. Because, do you have anything better to do? Why not pick the best thing possible that you could do? Because you're more powerful than you think, way more powerful than you think. I mean, God only knows what you are in the final analysis. You're blind to your own weaknesses, but you're also blind to your own strengths. How far could you take that if you stopped wasting time, and if you stopped lying, and if you oriented yourself to the highest possible good that you could conceive of and you committed to that? How much good could you do? Well, I would say: why don't you find out?"

SIZE
A high-resolution print size of 6' wide and 3' tall should provide ample space for both the quote and the accompanying artwork.

TYPOGRAPHY
Choose a bold, clean, and easily readable font for the quote. You could also experiment with different font sizes for certain words or phrases to emphasize their importance within the quote.

COLORS
Since the quote is thought-provoking and reflective, you might want to use a color palette that evokes a sense of introspection and depth. Consider using cool, calming colors like shades of blue, gray, or green. Alternatively, you can use a contrasting color scheme with a light background and dark text to make the quote stand out.

ARTWORK
Select / create / edit background artwork to complement the quote.
While a great design might be minimalistic and/or greyscale, I'd really like to see some full color options. This might be anything from photography or graphics inspired by the ideas in the text, to abstract colors or illustrations that feel like the sentiment expressed.
The art should capture your attention and encourage you to read the text. The art should be visually appealing, both at a distance and up close, regardless of whether the text is read.
Updates

Having trouble confirming the exact print size.

Still looking for printing solution and final size confirmation.

Target Market(s)

Personal, business, office

Industry/Entity Type

None

Font styles to use
Sans Serif
Script

Requirements
Must have
• Entire quote, legible text, modern design, attractive artwork, approx 6ft wide and 3ft tall
Nice to have
• Different font (sizes) for certain words or phrases to emphasize their importance within the quote.

```html
<!DOCTYPE html>
<html lang="en">
<head>
<meta charset="utf-8">
<title>Why Don't You Find Out — Marcus Hallwell</title>
<link rel="stylesheet" href="https://fonts.googleapis.com/css2?family=Roboto+Condensed:wght@400;500;700&display=swap">
<style>
  :root {
    --sky-deep: #050b08;
    --sky-green: #0d261e;
    --sky-teal: #1d4a48;
    --sky-blue: #2a4f78;
    --milky-light: #9fb6c4;
    --nebula-warm: #c07a3e;
    --nebula-rose: #8a5a52;
    --cloud-grey: #a6aeac;
    --stair-dark: #0a0a0b;
    --text-teal: #8fd3d2;
    --text-white: #ffffff;
    --quote-mark: #707070;
  }
  * { margin: 0; padding: 0; box-sizing: border-box; }
  html, body { width: 1200px; height: 600px; overflow: hidden; background: var(--sky-deep); }
  .artwork {
    position: relative;
    width: 1200px;
    height: 600px;
    overflow: hidden;
    font-family: "Roboto Condensed", "Arial Narrow", sans-serif;
  }
  .cosmic-scene {
    position: absolute; inset: 0;
    background:
      radial-gradient(ellipse 150px 120px at 140px 420px, rgba(220,225,230,0.55), transparent 70%),
      radial-gradient(ellipse 90px 80px at 30px 410px, rgba(190,200,210,0.45), transparent 70%),
      radial-gradient(ellipse 170px 160px at 130px 560px, rgba(10,10,11,0.95), transparent 75%),
      radial-gradient(ellipse 90px 110px at 125px 280px, rgba(192,122,62,0.75), transparent 72%),
      radial-gradient(ellipse 80px 140px at 90px 200px, rgba(138,90,82,0.55), transparent 72%),
      radial-gradient(ellipse 110px 70px at 1120px 490px, rgba(166,174,172,0.6), transparent 72%),
      radial-gradient(ellipse 260px 120px at 560px 590px, rgba(110,80,50,0.35), transparent 75%),
      radial-gradient(ellipse 170px 380px at 70px 150px, rgba(159,182,196,0.45), transparent 72%),
      radial-gradient(ellipse 360px 520px at 40px 120px, rgba(42,79,120,0.85), transparent 75%),
      radial-gradient(ellipse 700px 400px at 420px 250px, rgba(29,74,72,0.55), transparent 75%),
      linear-gradient(160deg, var(--sky-blue) 0%, var(--sky-green) 38%, var(--sky-deep) 100%);
  }
  .quote-mark {
    position: absolute;
    color: var(--quote-mark);
    font-weight: 700;
    font-size: 100px;
    line-height: 1;
  }
  .quote-mark--open { left: 56px; top: 24px; }
  .quote-mark--close { left: 916px; top: 508px; }
  .quote {
    position: absolute;
    left: 72px;
    top: 66px;
    width: 1128px;
    text-align: center;
    font-size: 33px;
    font-weight: 400;
    line-height: 38.6px;
  }
  .quote__line {
    display: block;
    white-space: nowrap;
    color: transparent;
    background: linear-gradient(90deg, var(--text-white) 0%, var(--text-white) 20%, var(--text-teal) 40%, var(--text-teal) 100%);
    -webkit-background-clip: text;
    background-clip: text;
    width: max-content;
    margin: 0 auto;
  }
  .quote__emphasis { color: var(--text-white); }
</style>
</head>
<body>
  <main class="artwork">
    <div class="cosmic-scene" role="img" aria-label="Starry night sky with the colourful Milky Way, a stone stairway rising through glowing clouds with a figure meditating at the top, and clouds on the lower right"></div>

    <span class="quote-mark quote-mark--open" aria-hidden="true">&ldquo;</span>

    <blockquote class="quote">
      <span class="quote__line">The thing that's so interesting about being alive is that you're all in. No matter what</span>
      <span class="quote__line">you do, you're all in. This is gonna kill you, so I think you might as well play the</span>
      <span class="quote__line">most magnificent game you can while you're waiting. Because, do you have</span>
      <span class="quote__line">anything better to do? Why not pick the best thing possible that you could</span>
      <span class="quote__line">do? <span class="quote__emphasis">Because you're more powerful than you think,</span> way more powerful</span>
      <span class="quote__line">than you think. I mean, God only knows what you are in the final analysis.</span>
      <span class="quote__line">You're blind to your own weaknesses, but you're also blind to your</span>
      <span class="quote__line">own strengths. How far could you take that if you stopped wasting</span>
      <span class="quote__line">time, and if you stopped lying, and if you oriented yourself</span>
      <span class="quote__line">to the highest possible good that you could conceive of and</span>
      <span class="quote__line">you committed to that? How much good could you do?</span>
      <span class="quote__line">Well, I would say: <span class="quote__emphasis">why don't you find out?</span></span>
    </blockquote>

    <span class="quote-mark quote-mark--close" aria-hidden="true">&rdquo;</span>
  </main>
</body>
</html>
```